Texas-Based Roofing Company Looking for Creative Billboard Design

We need a billboard designed for a roofing company in the Dallas - Fort Worth area. They are a tech-forward company that uses drone technology to complete roof inspections. We would like to see a design that is out-of-the-box in terms of creativity. It can be marketed towards a hail/wind storm event, or a creative approach to helping customers think of VORTANIC when it comes to roofing needs.
Updates

Low design quality

Target Market(s)

residential homeowners

Industry/Entity Type

Roofing

Requirements
Must have
• Creative approach or play on words to elevate brand awareness.

```html
<!DOCTYPE html>
<html lang="en">
<head>
<meta charset="utf-8">
<title>Vortanic Roofing Billboard</title>
<link href="https://fonts.googleapis.com/css2?family=Barlow+Condensed:wght@600;700&family=Lato:wght@400&display=swap" rel="stylesheet">
<style>
  :root {
    --navy: #0f3b68;
    --sky-blue: #5c90bf;
    --gold: #e6b021;
    --ink: #1f1f1f;
    --white: #ffffff;
    --house-dark: #2c3550;
    --house-mid: #6f7890;
    --house-warm: #d9a35a;
  }
  html, body {
    margin: 0;
    padding: 0;
    width: 1200px;
    height: 506px;
    overflow: hidden;
    background: var(--white);
  }
  .billboard {
    position: relative;
    width: 1200px;
    height: 506px;
    overflow: hidden;
    background: var(--white);
    font-family: "Lato", sans-serif;
  }
  .billboard__shapes {
    position: absolute;
    inset: 0;
    width: 1200px;
    height: 506px;
  }
  .headline {
    position: absolute;
    left: 62px;
    top: 52px;
    margin: 0;
    font-family: "Barlow Condensed", sans-serif;
    font-weight: 700;
    font-size: 88px;
    line-height: 1;
    color: var(--white);
    letter-spacing: 0.5px;
    white-space: nowrap;
  }
  .headline__bang {
    display: inline-block;
    margin-left: 16px;
    font-size: 104px;
    vertical-align: -6px;
  }
  .hazards {
    position: absolute;
    left: 62px;
    top: 158px;
    display: flex;
    gap: 28px;
    margin: 0;
    padding: 0;
    list-style: none;
  }
  .hazards__item {
    display: flex;
    align-items: center;
    gap: 12px;
    font-family: "Barlow Condensed", sans-serif;
    font-weight: 700;
    font-size: 46px;
    line-height: 1;
    color: var(--white);
  }
  .hazards__icon {
    width: 36px;
    height: 36px;
    flex: none;
  }
  .brand {
    position: absolute;
    left: 770px;
    top: 206px;
    width: 420px;
    text-align: center;
  }
  .brand__name {
    margin: 0;
    font-family: "Lato", sans-serif;
    font-weight: 400;
    font-size: 61px;
    line-height: 1.02;
    letter-spacing: 5px;
    color: var(--ink);
  }
  .brand__tagline {
    margin: 12px 0 0;
    font-family: "Lato", sans-serif;
    font-weight: 400;
    font-size: 18px;
    line-height: 1.85;
    letter-spacing: 3.4px;
    color: var(--gold);
  }
</style>
</head>
<body>
<main class="billboard">
  <svg class="billboard__shapes" viewBox="0 0 1500 632" preserveAspectRatio="none">
    <defs>
      <linearGradient id="houseTone" x1="0" y1="0" x2="0.4" y2="1">
        <stop offset="0" stop-color="#2c3550"/>
        <stop offset="0.45" stop-color="#6f7890"/>
        <stop offset="1" stop-color="#d9a35a"/>
      </linearGradient>
    </defs>
    <polygon class="band band--navy" points="0,0 1062,0 430,632 0,632" fill="#0f3b68"/>
    <polygon class="band band--navy-thin" points="1088,0 1160,0 528,632 456,632" fill="#0f3b68"/>
    <polygon class="band band--sky" points="906,295 958,295 620,632 568,632" fill="#5c90bf"/>
    <polygon class="band band--gold" points="832,443 892,443 703,632 643,632" fill="#e6b021"/>
    <polygon class="house-photo" role="img" aria-label="Photo of a two-storey suburban house at dusk with lit windows"
             points="0,300 762,300 430,632 0,632" fill="url(#houseTone)"/>
  </svg>

  <h1 class="headline">WE CAN FIX THAT<span class="headline__bang">!</span></h1>

  <ul class="hazards">
    <li class="hazards__item">
      <svg class="hazards__icon" viewBox="0 0 36 36" aria-hidden="true">
        <polygon points="18,4 25,8 25,16 18,20 11,16 11,8" fill="var(--gold)"/>
        <polygon points="9,18 16,22 16,30 9,34 2,30 2,22" fill="var(--gold)"/>
        <polygon points="27,18 34,22 34,30 27,34 20,30 20,22" fill="var(--gold)"/>
      </svg>
      HAIL
    </li>
    <li class="hazards__item">
      <svg class="hazards__icon" viewBox="0 0 36 36" aria-hidden="true">
        <g fill="none" stroke="var(--gold)" stroke-width="4" stroke-linecap="round">
          <path d="M3 9 Q10 5 18 9 T33 9"/>
          <path d="M3 18 Q10 14 18 18 T33 18"/>
          <path d="M3 27 Q10 23 18 27 T33 27"/>
        </g>
      </svg>
      WIND
    </li>
    <li class="hazards__item">
      <svg class="hazards__icon" viewBox="0 0 36 36" aria-hidden="true">
        <polygon points="22,1 7,21 17,21 12,35 29,13 19,13 26,1" fill="var(--gold)"/>
      </svg>
      STORM
    </li>
  </ul>

  <section class="brand">
    <p class="brand__name">VORTANIC<br>ROOFING</p>
    <p class="brand__tagline">PROTECTING YOUR HOME<br>THROUGH EVERY STORM</p>
  </section>
</main>
</body>
</html>
```